Design a Flyer for new years eve

Celebrate (ring in) new years at Corvina Restaurant
Call to make a reservation (206) 583 - 2914

Featuring Dominic Hale with Acoustic Guitar (nights live entertainment)

Materials could be found
www.corvinabistro.com
www.facebook.com/corvinabistro
www.instagram.com/corvinabistro

Dominic's only picture we have is the one uploaded, feel free to search the web for more if you want.

We want a flyer that is elegant and reflects the ambiance of a classy Mediterranean restaurant.

```html
<!DOCTYPE html>
<html lang="en">
<head>
<meta charset="utf-8">
<title>NYE Flyer – Corvina Restaurant</title>
<link rel="stylesheet" href="https://fonts.googleapis.com/css2?family=Alfa+Slab+One&family=Montserrat:wght@500;600;700&family=Oswald:wght@400;500;600&display=swap">
<style>
  :root {
    --stage: #dcd9dc;
    --night: #07070a;
    --ink: #ffffff;
    --neon-pink: #ff3fb4;
    --neon-blue: #5fd8ff;
    --hot-pink: #f2198f;
    --gold: #f2a93b;
    --silver: #d9d9de;
    --rule: #2d8fb8;
  }
  * { margin: 0; padding: 0; box-sizing: border-box; }
  html, body { width: 1200px; height: 900px; overflow: hidden; }
  body { background: var(--stage); position: relative; font-family: "Montserrat", sans-serif; }

  .flyer {
    position: absolute; left: 290px; top: 39px;
    width: 620px; height: 822px;
    background: var(--night);
    overflow: hidden;
    box-shadow: 0 6px 18px rgba(0,0,0,.35);
  }
  .flyer__photo {
    position: absolute; inset: 0 0 300px 0;
    background:
      radial-gradient(ellipse at 22% 30%, rgba(255,150,60,.55), transparent 55%),
      radial-gradient(ellipse at 18% 62%, rgba(255,60,170,.55), transparent 45%),
      radial-gradient(ellipse at 75% 40%, rgba(120,70,40,.5), transparent 60%),
      linear-gradient(180deg, #2a160c 0%, #3b1d10 45%, #07070a 100%);
  }
  .flyer__fade {
    position: absolute; left: 0; right: 0; top: 380px; height: 200px;
    background: linear-gradient(180deg, transparent, var(--night));
  }

  .brand { position: absolute; top: 40px; width: 100%; text-align: center; }
  .brand__dot {
    width: 22px; height: 22px; border-radius: 50%;
    background: var(--ink); margin: 0 auto 12px;
  }
  .brand__name {
    font-weight: 700; color: var(--ink);
    font-size: 46px; letter-spacing: 5px; line-height: 1;
  }
  .brand__name span { display: block; font-size: 19px; letter-spacing: 4px; margin-top: 10px; }

  .neon-frame { position: absolute; left: 90px; top: 262px; width: 440px; height: 280px; }
  .neon-frame rect { fill: none; }

  .nye {
    position: absolute; top: 282px; width: 100%; text-align: center;
    font-family: "Alfa Slab One", serif; font-size: 112px; line-height: 1;
    color: transparent; -webkit-text-stroke: 3px var(--ink);
    letter-spacing: 4px;
    text-shadow: 0 0 10px var(--neon-pink), 0 0 22px var(--neon-pink);
  }
  .year {
    position: absolute; top: 410px; width: 100%;
    display: flex; justify-content: center; align-items: center; gap: 4px;
    font-family: "Alfa Slab One", serif; font-size: 96px; line-height: 1;
    color: transparent; -webkit-text-stroke: 3px var(--ink);
    text-shadow: 0 0 10px var(--neon-pink), 0 0 20px var(--neon-pink);
  }
  .year__ball {
    width: 84px; height: 84px; border-radius: 50%;
    background: radial-gradient(circle at 35% 35%, #ffd0f0, #ff4fc0 40%, #8a1a8f 100%);
    box-shadow: 0 0 22px var(--neon-pink);
  }

  .celebrate {
    position: absolute; left: 106px; top: 515px; width: 390px; height: 82px;
    border: 3px dotted var(--ink);
    box-shadow: 0 0 10px var(--neon-blue), inset 0 0 10px var(--neon-blue);
    text-align: center; color: var(--ink);
    display: flex; flex-direction: column; justify-content: center;
  }
  .celebrate__lead { font-weight: 600; font-size: 18px; letter-spacing: .5px; }
  .celebrate__lead span { margin: 0 8px; }
  .celebrate__venue { font-weight: 700; font-size: 27px; letter-spacing: .5px; line-height: 1.15; }

  .featuring {
    position: absolute; left: 238px; top: 609px; width: 140px; height: 30px;
    background: var(--hot-pink); color: var(--ink);
    font-weight: 700; font-size: 19px; text-align: center; line-height: 30px;
  }
  .artist {
    position: absolute; top: 650px; width: 100%; text-align: center;
    font-family: "Oswald", sans-serif; color: var(--silver);
  }
  .artist__name { font-size: 38px; font-weight: 500; letter-spacing: 1px; }
  .artist__with { font-size: 22px; font-weight: 400; }

  .date {
    position: absolute; top: 702px; width: 100%; text-align: center;
    font-family: "Oswald", sans-serif; font-weight: 600; font-size: 30px;
    color: var(--gold); letter-spacing: .5px;
  }
  .date__stars { font-size: 16px; vertical-align: middle; margin: 0 18px; letter-spacing: 3px; }

  .reserve {
    position: absolute; top: 742px; width: 100%; text-align: center;
    font-family: "Oswald", sans-serif; font-weight: 500; font-size: 29px;
    color: var(--silver); letter-spacing: .5px;
  }

  .links {
    position: absolute; left: 20px; right: 20px; bottom: 8px; height: 30px;
    border-top: 1px solid var(--rule); border-bottom: 1px solid var(--rule);
    display: flex; justify-content: space-between; align-items: center;
    font-size: 11.5px; font-weight: 500; color: var(--ink);
  }
  .links span + span { border-left: 1px solid var(--rule); padding-left: 8px; }
</style>
</head>
<body>
  <main class="flyer">
    <div class="flyer__photo" role="img" aria-label="Motion-blurred photo of a guitarist performing under warm restaurant lights"></div>
    <div class="flyer__fade"></div>

    <header class="brand">
      <div class="brand__dot"></div>
      <div class="brand__name">CORVINA<span>RESTAURANT</span></div>
    </header>

    <svg class="neon-frame" viewBox="0 0 440 280" aria-hidden="true">
      <rect x="6" y="6" width="428" height="140" rx="18" stroke="#ffffff" stroke-width="3" style="filter: drop-shadow(0 0 5px #5fd8ff)"/>
      <rect x="24" y="120" width="410" height="100" rx="16" stroke="#ff3fb4" stroke-width="2.5" style="filter: drop-shadow(0 0 5px #ff3fb4)"/>
    </svg>

    <div class="nye">NYE</div>
    <div class="year">2<div class="year__ball" role="img" aria-label="Glowing pink mirror disco ball"></div>18</div>

    <section class="celebrate">
      <div class="celebrate__lead"><span>CELEBRATE</span><span>NEW YEARS</span></div>
      <div class="celebrate__venue">CORVINA RESTAURANT</div>
    </section>

    <div class="featuring">FEATURING:</div>
    <div class="artist"><span class="artist__name">DOMINIC HALE</span> <span class="artist__with">WITH (ACOUSTIC GUITAR)</span></div>
    <div class="date"><span class="date__stars">★★★</span>SUNDAY 31ST DECEMBER<span class="date__stars">★★★</span></div>
    <div class="reserve">RESERVATION: (206) 583 - 2914</div>

    <footer class="links">
      <span>www.corvinabistro.com</span>
      <span>www.facebook.com/corvinabistro</span>
      <span>www.instagram.com/corvinabistro</span>
    </footer>
  </main>
</body>
</html>
```